Quarveling stickers design for our main topics (for example: agile and Kanban)

We are looking for sticker design, that will reflect our cooperate identity and can be used for the different topics in our company. We would like to start with our Agile Coaching Offers with a Kanban Sticker saying "stop starting, start finishing", A bad example can be find in the file upload ;)
Check out our homepage to get a feeling for the cooperate identity (www.quarveling.ch)

Target Market(s)

Customers and trainees from our trainings

Industry/Entity Type

Consulting

Colors
0355a3
fbed22

Requirements
Must have
• a cool design thats fits to our customer design
the 2 lines can be changed for future stickers ... like in the example "stop starting, start finishing" and "we show you how"
Nice to have
• -
Should not have
• -

```html
<!DOCTYPE html>
<html lang="en">
<head>
<meta charset="utf-8">
<title>Quarveling sticker – stop starting, start finishing</title>
<link rel="stylesheet" href="https://fonts.googleapis.com/css2?family=Cabin:wght@400;600&display=swap">
<style>
  :root {
    --brand-blue: #0355a3;
    --brand-yellow: #fbed22;
    --paper: #ffffff;
    --ink: #111111;
  }
  html, body {
    margin: 0;
    padding: 0;
    overflow: hidden;
    background: var(--paper);
  }
  .sticker {
    position: relative;
    width: 1200px;
    height: 368px;
    overflow: hidden;
    font-family: "Cabin", "Candara", sans-serif;
  }
  .headline-panel {
    position: absolute;
    left: 0;
    top: 0;
    width: 780px;
    height: 368px;
    background: var(--brand-blue);
  }
  .headline {
    position: absolute;
    left: 64px;
    top: 58px;
    margin: 0;
    color: var(--brand-yellow);
    font-weight: 600;
    font-size: 106px;
    line-height: 130px;
    letter-spacing: -1px;
  }
  .headline span { display: block; white-space: nowrap; }
  .tagline-panel {
    position: absolute;
    left: 780px;
    top: 0;
    width: 420px;
    height: 219px;
    background: var(--brand-yellow);
  }
  .tagline {
    position: absolute;
    left: 0;
    right: 0;
    top: 44px;
    margin: 0;
    text-align: center;
    color: var(--brand-blue);
    font-weight: 600;
    font-size: 62px;
    line-height: 72px;
    letter-spacing: -1px;
  }
  .tagline span { display: block; }
  .company-panel {
    position: absolute;
    left: 780px;
    top: 219px;
    width: 420px;
    height: 149px;
    background: var(--paper);
  }
  .company-mark {
    position: absolute;
    left: 40px;
    top: 40px;
    width: 68px;
    height: 68px;
    background: var(--brand-blue);
  }
  .company-name {
    position: absolute;
    left: 128px;
    top: 18px;
    margin: 0;
    color: var(--ink);
    font-weight: 400;
    font-size: 40px;
    line-height: 48px;
    white-space: nowrap;
  }
</style>
</head>
<body>
  <div class="sticker">
    <section class="headline-panel">
      <h1 class="headline">
        <span>stop starting,</span>
        <span>start finishing</span>
      </h1>
    </section>
    <section class="tagline-panel">
      <p class="tagline">
        <span>we show you</span>
        <span>how</span>
      </p>
    </section>
    <section class="company-panel">
      <div class="company-mark" aria-hidden="true"></div>
      <p class="company-name">quarveling ag</p>
    </section>
  </div>
</body>
</html>
```